Aviation Maintenance & Aircraft Cleaning Website

We need a fairly simple modern sleek website . Our company does aviation maintenance , aircraft cleaning , maintenance tracking . We work on KT420 HELICOPTERS , BELVANKO T82 HELICOPTERS , MORVELL TARRANT 512 HELICOPTERS. We would like a website that can be mobile as well with future ideas that an app where you could book cleanings and maintenance . Right now the biggest thing is for our customer to see a website , be able to book our services online and see our staff . the website must be modern and clean .

Target Market(s)

Aviation maintenance , aviation cleaning ,

Logo Text

TW but 1 image unlike the one i uploaded which is two . Im open for different aviation designs

Number of Pages Required

5+ page

Font styles to use
Serif

Requirements
Must have
• Home page , Aircraft Maintenance , Aircraft Cleaning , About Us , Contact , Careers

TW Aviation is insured and all of our mechanics are licensed by the NQB with an Airframe & Powerplant rating. ( FRONT PAGE )

Home page should have a simple nice picture of a KT420 or Belvanko T82 . My Logo as you can see seems like two logos . i would like 1 logo and made of the two if possible . (New ideas are welcome . )

Book a Cleaning Calendar should in the aircraft cleaning page . The aircraft cleaning page should have a picture of cleaning a helicopter or private jet .

Aircraft maintenance page should have a mechanic working on a helicopter . The Page should have a fast way to contact us .

We are a mobile AOG team who is available 24/7 . What we do
Scheduled & Unscheduled aircraft maintenance
Major & Minor repairs
STC installations
Aircraft Weight & Balance
Aircraft Painting
Aircraft Cleaning
Maintenance Tracking Utilizing Tracking Programs or spreadsheets
Removal & Installation of Components
Aircraft Pre Buy Inspections
Nice to have
• modern , sleek , aviation

Meet the Staff

Picture with Headset on flying in a helicopter

CEO Mateus Ferreira

Mateus Has been an aircraft mechanic for over 10 years . He has worked for the largest sightseeing & charter tourism company in the New York City area as well as repair stations & manufacturers. He has aircraft specific training to the Kestrane KT420 & Vornel 2K4. He has worked on several airframes including the Belvanko T82 and the Morvell 512. He has held every position in an aircraft maintenance department from mechanic up to Director of Maintenance . His work ethic and ability to manage mechanics in a organized and structured way gives any department or inspection a clear direction .

About Us

TW Aviation Services is company with aircraft maintenance experience . We focus on inspections of aircraft . Our Aircraft Mechanics who are pilots and IA's have experience many aircraft but specialize in the Kestrane KT420 , KT425 , KT435 . The Belvanko T82 and Morvell Tarrant 512 . Our focus is safety and to maintain aircraft day in and day out so our customer can operate the aircraft safely while keeping up with all the manufacturers inspections .

We know aircraft maintenance & maintenance planning . Leave the technical and tedious things to us . Get in your aircraft and fly knowing you have the best maintenance crew in the business.

```html
<!DOCTYPE html>
<html lang="en">
<head>
<meta charset="utf-8">
<title>TW Aviation – Careers</title>
<link href="https://fonts.googleapis.com/css2?family=Montserrat:wght@400;500;600&family=Playfair+Display:wght@600;700&display=swap" rel="stylesheet">
<style>
:root{
  --navy:#0c1730;
  --blue:#213f8e;
  --ink:#1a1a1a;
  --muted:#8a8a8a;
  --rule:#bdbdbd;
  --white:#ffffff;
  --grey-tab:#7a7a7a;
}
*{margin:0;padding:0;box-sizing:border-box}
html,body{width:1200px;height:2908px;overflow:hidden;background:var(--white)}
body{position:relative;font-family:'Montserrat',sans-serif;color:var(--ink)}
.abs{position:absolute}
.serif{font-family:'Playfair Display',serif}

/* header */
.site-header{position:absolute;left:0;top:0;width:1200px;height:67px;background:var(--white)}
.brand{position:absolute;left:122px;top:20px;display:flex;align-items:center;gap:8px;font-weight:600;font-size:18px;color:var(--blue);letter-spacing:1px}
.brand-mark{width:14px;height:14px;background:var(--blue)}
.nav a{position:absolute;top:24px;font-size:15.5px;color:#333;text-decoration:none}
.nav a.active{color:var(--blue);border-bottom:1.5px solid var(--blue);padding-bottom:3px}
.nav .nav-cta{top:17px;left:954px;width:121px;height:34px;background:var(--blue);color:var(--white);display:flex;align-items:center;justify-content:center}

/* hero */
.hero-panel{left:0;top:67px;width:446px;height:405px;background:var(--navy)}
.hero-title{left:125px;top:196px;font-size:43px;line-height:53px;color:var(--white);font-weight:700}
.btn{display:flex;align-items:center;justify-content:center;background:var(--blue);color:var(--white);font-size:15.5px}
.hero-btn{left:125px;top:318px;width:136px;height:35px}
.hero-photo{left:446px;top:67px;width:754px;height:405px;background:linear-gradient(120deg,#3a3633,#6f6c69 45%,#d6d7d9 70%,#4a4d56)}

/* section headings */
.section-title{left:0;width:1200px;text-align:center;font-size:46px;font-weight:700;color:var(--ink)}
.rule{height:2px;background:var(--ink)}

/* perks */
.perk h3{font-size:21px;font-weight:600;color:var(--blue)}
.perk p{margin-top:9px;margin-left:2px;font-size:12.3px;line-height:17.5px;color:#444;width:270px}

/* gallery */
.gallery{left:0;top:1275px;width:1200px;height:399px;display:flex}
.gallery div{flex:1}

/* tabs */
.tab{top:1956px;font-size:21px;font-weight:600;color:var(--grey-tab)}
.tab.active{color:var(--blue);border-bottom:2px solid var(--blue);padding-bottom:1px}

/* job list */
.job{left:125px;width:871px;height:110px;border-bottom:1px solid var(--rule)}
.job h4{position:absolute;left:3px;top:12px;font-size:16px;font-weight:600;letter-spacing:.4px;color:#222}
.job span{position:absolute;left:3px;top:39px;font-size:12px;color:var(--muted);letter-spacing:.3px}
.job .btn{position:absolute;left:741px;top:25px;width:129px;height:42px}

/* footer */
.to-top{left:1013px;top:2609px}
.site-footer{left:0;top:2642px;width:1200px;height:266px;background:var(--navy);color:var(--white)}
.foot-brand{position:absolute;left:122px;top:46px;display:flex;align-items:center;gap:10px;font-size:24px;font-weight:600;letter-spacing:1.5px}
.foot-brand .brand-mark{width:20px;height:20px;background:var(--white)}
.contact-line{position:absolute;left:128px;display:flex;align-items:center;gap:8px;font-size:15px;font-weight:500}
.socials{position:absolute;left:131px;top:204px;display:flex;gap:30px}
.socials span{width:16px;height:16px;border-radius:50%;background:var(--white)}
.foot-col{position:absolute;top:78px}
.foot-col h5{font-size:16px;font-weight:600}
.foot-col a{display:block;margin-top:26px;font-size:15.5px;color:#d8dbe3;text-decoration:none}
.copyright{position:absolute;right:24px;top:227px;font-size:10px;color:#c9ccd6}
</style>
</head>
<body>

<header class="site-header">
  <div class="brand"><span class="brand-mark"></span>TW AVIATION</div>
  <nav class="nav">
    <a style="left:359px">Home</a>
    <a style="left:456px">About Us</a>
    <a style="left:576px">Maintenance</a>
    <a style="left:725px">Cleaning</a>
    <a class="active" style="left:842px">Careers</a>
    <a class="nav-cta">Contact Us</a>
  </nav>
</header>

<section>
  <div class="abs hero-panel"></div>
  <h1 class="abs hero-title serif">Let’s Work<br>With Us</h1>
  <a class="abs btn hero-btn">View Jobs</a>
  <div class="abs hero-photo" role="img" aria-label="Two mechanics working on a white helicopter in a hangar"></div>
</section>

<section>
  <div class="abs rule" style="left:209px;top:624px;width:148px"></div>
  <h2 class="abs section-title serif" style="top:588px">About Working Here</h2>
  <div class="abs rule" style="left:842px;top:624px;width:147px"></div>

  <div class="abs perk" style="left:285px;top:748px"><h3>Conducive Environtment</h3><p>Enjoy challenging work and a satisfying job without any hierarchy</p></div>
  <div class="abs perk" style="left:691px;top:748px"><h3>Shared Success</h3><p>Equity ownership and opportunity await</p></div>
  <div class="abs perk" style="left:285px;top:903px"><h3>Healthy Meals and Snacks</h3><p>Food is in the house so it feels like home</p></div>
  <div class="abs perk" style="left:691px;top:903px"><h3>Medical Insurance</h3><p>We’ve got you covered, literally!</p></div>
  <div class="abs perk" style="left:285px;top:1053px"><h3>Best Gadgets</h3><p>Pamper the tech savvy in you with gadgets and advanced technology</p></div>
  <div class="abs perk" style="left:691px;top:1053px"><h3>Culture of Learning</h3><p>Regular brown bag lunches to keep the brain rejuvenated</p></div>
</section>

<section class="abs gallery">
  <div role="img" aria-label="Mechanic inspecting a helicopter engine" style="background:linear-gradient(135deg,#2e3038,#7d7a78 55%,#c9bdb4)"></div>
  <div role="img" aria-label="Technicians working on a helicopter gearbox in a hangar" style="background:linear-gradient(160deg,#b8b6b2,#8c8578 50%,#d3d1cc)"></div>
  <div role="img" aria-label="Pilot wearing a headset in a helicopter cockpit" style="background:linear-gradient(200deg,#c7c9cc,#5b5d63 50%,#3b3f4a)"></div>
</section>

<section>
  <div class="abs rule" style="left:226px;top:1834px;width:147px"></div>
  <h2 class="abs section-title serif" style="top:1798px">Open Positions</h2>
  <div class="abs rule" style="left:825px;top:1834px;width:147px"></div>

  <span class="abs tab active serif" style="left:125px">Technician</span>
  <span class="abs tab serif" style="left:344px">Marketing</span>
  <span class="abs tab serif" style="left:565px">Finance</span>
  <span class="abs tab serif" style="left:759px">Other</span>

  <div class="abs job" style="top:2034px"><h4>Aircraft Technician</h4><span>Sans Fransisco, Full Time</span><a class="btn">Apply Now</a></div>
  <div class="abs job" style="top:2144px"><h4>Aircraft Technician</h4><span>New Delhi, Part Time</span><a class="btn">Apply Now</a></div>
  <div class="abs job" style="top:2254px"><h4>Technical Trainer</h4><span>Sans Fransisco, Full Time</span><a class="btn">Apply Now</a></div>
  <div class="abs job" style="top:2364px"><h4>Technician Suppervisor</h4><span>Sans Fransisco, Full Time</span><a class="btn">Apply Now</a></div>
</section>

<svg class="abs to-top" width="62" height="33" viewBox="0 0 62 33" aria-label="Back to top"><polygon points="31,0 62,33 0,33" fill="#213f8e"/></svg>

<footer class="abs site-footer">
  <div class="foot-brand"><span class="brand-mark"></span>TW AVIATION</div>
  <div class="contact-line" style="top:135px">
    <svg width="16" height="16" viewBox="0 0 24 24"><path fill="#fff" d="M6.6 10.8a15.1 15.1 0 0 0 6.6 6.6l2.2-2.2c.3-.3.7-.4 1-.2 1.1.4 2.3.6 3.6.6.6 0 1 .4 1 1V20c0 .6-.4 1-1 1A17 17 0 0 1 3 4c0-.6.4-1 1-1h3.5c.6 0 1 .4 1 1 0 1.3.2 2.5.6 3.6.1.3 0 .7-.2 1z"/></svg>
    +555010240
  </div>
  <div class="contact-line" style="top:169px">
    <svg width="17" height="14" viewBox="0 0 24 20"><path fill="#fff" d="M2 0h20a2 2 0 0 1 2 2v16a2 2 0 0 1-2 2H2a2 2 0 0 1-2-2V2a2 2 0 0 1 2-2zm10 9 10-6V2L12 8 2 2v1z"/></svg>
    hello@twaviation.com
  </div>
  <div class="socials"><span aria-label="social link one"></span><span aria-label="social link two"></span><span aria-label="social link three"></span></div>

  <div class="foot-col" style="left:446px"><h5>About Us</h5><a>Meet Our Staff</a><a>Career</a></div>
  <div class="foot-col" style="left:659px"><h5>Contact Us</h5><a>FAQ</a><a>Blog</a></div>
  <div class="foot-col" style="left:834px"><h5>Support</h5><a>Services</a><a>Procedures</a></div>
  <div class="copyright">©2020 TW AVIATION</div>
</footer>

</body>
</html>
```